Roadwise Beacon Traffic Control Company Website

Modern website Wordpress design using all greyscale photos with a pop of red (such as road closure signs or detour cones) for strategic emphasis. (see brand guide for color codes)
The creative goal is to leverage high-contrast, desaturated imagery to create a clean, professional, and industrial feel. The selective use of red will draw immediate attention to critical elements—such as road hazards, safety equipment, or key messages to ensure the viewer's focus is directed with purpose.

Brand guide, homepage content and logo are attached. Create clean professional user experience to market services to industry professionals.

```html
<!DOCTYPE html>
<html lang="en">
<head>
<meta charset="utf-8">
<title>Roadwise Beacon Traffic Control Company</title>
<link href="https://fonts.googleapis.com/css2?family=Archivo:wght@400;700;800&family=Manrope:wght@700;800&family=Inter:wght@400;500&display=swap" rel="stylesheet">
<style>
  :root{
    --red:#e8222b;
    --ink:#111111;
    --white:#ffffff;
    --band:#585858;
    --footer:#5a5a5a;
    --muted:#3c3c3c;
    --light:#e9e9e9;
  }
  *{margin:0;padding:0;box-sizing:border-box}
  html,body{width:814px;height:1200px;overflow:hidden;background:var(--white)}
  body{position:relative;font-family:"Inter",Arial,sans-serif;color:var(--ink)}

  /* Header */
  .site-header{position:absolute;left:0;top:0;width:814px;height:61px;background:var(--white)}
  .nav-link{position:absolute;top:24px;font-size:9.5px;letter-spacing:.2px;color:var(--ink);text-decoration:none}
  .nav-link.is-active{color:var(--red)}
  .nav-link.is-active::after{content:"";position:absolute;left:-1px;right:-1px;top:14px;height:3px;background:var(--red)}
  .brand{position:absolute;left:357px;top:17px;width:100px;text-align:center}
  .brand-name{font-family:"Archivo",sans-serif;font-weight:800;font-size:11px;line-height:13px;letter-spacing:.5px;color:var(--ink)}
  .brand-bar{display:block;width:64px;height:6px;margin:4px auto 0;background:var(--red)}

  /* Hero */
  .hero{position:absolute;left:0;top:61px;width:814px;height:407px;overflow:hidden;
    background:
      linear-gradient(90deg,rgba(240,90,40,.55) 0,rgba(240,90,40,.45) 9%,rgba(0,0,0,0) 17%,rgba(0,0,0,0) 81%,rgba(240,90,40,.45) 89%,rgba(240,90,40,.55) 96%,rgba(0,0,0,0) 100%),
      linear-gradient(180deg,#4a4a4a 0,#5e5e5e 40%,#6a6a6a 70%,#545454 100%)}
  .hero-title{position:absolute;left:0;top:100px;width:830px;text-align:center;font-family:"Archivo",sans-serif;font-size:34px;line-height:38px;letter-spacing:.5px;color:var(--white)}
  .hero-title .strong{font-weight:800}
  .hero-title .accent{font-weight:400;color:var(--red)}
  .hero-cta{position:absolute;left:369px;top:267px;width:94px;height:30px;border-radius:8px;background:var(--red);color:var(--white);font-family:"Archivo",sans-serif;font-weight:700;font-size:11px;letter-spacing:.3px;line-height:30px;text-align:center}

  /* Services */
  .services-title{position:absolute;left:0;top:513px;width:814px;text-align:center;font-family:"Archivo",sans-serif;font-weight:800;font-size:23px;letter-spacing:.5px;color:var(--ink)}
  .services-sub{position:absolute;left:0;top:548px;width:814px;text-align:center;font-size:8.4px;color:var(--muted);letter-spacing:.1px}

  .hex{position:absolute;width:178px;height:157px;
    clip-path:polygon(25% 0,75% 0,100% 50%,75% 100%,25% 100%,0 50%)}
  .hex-photo{position:absolute;left:0;top:0;width:100%;height:69%}
  .hex-label{position:absolute;left:0;top:69%;width:100%;height:31%;background:var(--band);
    display:flex;align-items:center;justify-content:center;text-align:center;
    font-family:"Manrope",sans-serif;font-weight:800;font-size:10.5px;line-height:13px;color:var(--white)}
  .hex-feature{background:linear-gradient(180deg,#8a8a8a 0,#c9a0a0 35%,#e8222b 70%,#e8222b 100%)}
  .hex-feature .hex-label{top:42%;height:58%;background:none;font-size:11.5px;line-height:14.5px;padding:0 22px 14px}

  .tone-a{background:linear-gradient(160deg,#3a3a3a,#7a7a7a 55%,#c94a4a)}
  .tone-b{background:linear-gradient(180deg,#6b6b6b,#4a4a4a 40%,#d9461f 60%,#555)}
  .tone-c{background:radial-gradient(circle at 52% 55%,#d42a2a 0 22%,#b9b9b9 23%,#8d8d8d 100%)}
  .tone-d{background:radial-gradient(circle at 55% 70%,#f07a20 0 35%,#7d7d7d 36%,#5b5b5b 100%)}
  .tone-e{background:radial-gradient(circle at 50% 60%,#ee8a2c 0 38%,#c9c9c9 39%,#8a8a8a 100%)}
  .tone-f{background:radial-gradient(circle at 50% 55%,#ea8a2a 0 40%,#8b8b8b 41%,#5e5e5e 100%)}
  .tone-g{background:linear-gradient(90deg,#5a5a5a,#ff5a2a 30%,#9a9a9a 45%,#444 100%)}

  /* Footer */
  .site-footer{position:absolute;left:0;top:946px;width:814px;height:254px;background:var(--footer);color:var(--white)}
  .footer-brand{position:absolute;left:41px;top:32px;font-family:"Archivo",sans-serif;font-weight:800;font-size:12px;line-height:14px;letter-spacing:.5px;color:var(--white)}
  .footer-brand .brand-bar{margin:5px 0 0;width:51px}
  .footer-tagline{position:absolute;left:42px;top:85px;width:240px;font-size:8.6px;line-height:14px;color:var(--light)}
  .partners{position:absolute;left:41px;top:126px;display:flex;gap:22px;align-items:center}
  .partner{background:var(--light);opacity:.85}
  .partner.sq{width:52px;height:38px;border-radius:4px}
  .partner.wide{width:100px;height:20px;border-radius:10px}
  .partner.round{width:46px;height:46px;border-radius:50%}
  .footer-divider{position:absolute;left:467px;top:25px;width:1px;height:145px;background:#777}
  .footer-heading{position:absolute;left:494px;top:28px;font-family:"Manrope",sans-serif;font-weight:800;font-size:12px;color:var(--white)}
  .footer-heading::after{content:"";position:absolute;left:0;top:21px;width:24px;height:3px;background:var(--red)}
  .footer-list{position:absolute;left:494px;top:67px;list-style:none;font-size:8.6px;color:var(--light)}
  .footer-list li{position:relative;padding-left:15px;height:17.8px}
  .footer-list li::before{content:"";position:absolute;left:0;top:3px;width:6px;height:6px;background:var(--red)}
  .footer-rule{position:absolute;left:41px;top:212px;width:732px;height:1px;background:#777}
  .copyright{position:absolute;left:0;top:227px;width:814px;text-align:center;font-size:8.4px;color:var(--light)}
</style>
</head>
<body>

<header class="site-header">
  <a class="nav-link is-active" style="left:42px">HOME</a>
  <a class="nav-link" style="left:104px">ABOUT</a>
  <a class="nav-link" style="left:171px">SERVICES</a>
  <div class="brand">
    <div class="brand-name">ROADWISE<br>BEACON</div>
    <span class="brand-bar"></span>
  </div>
  <a class="nav-link" style="left:589px">RENTALS</a>
  <a class="nav-link" style="left:668px">JOBS</a>
  <a class="nav-link" style="left:728px">CONTACT</a>
</header>

<section class="hero" role="img" aria-label="Greyscale road work scene with a truck and orange traffic cones on both sides">
  <h1 class="hero-title">
    <span class="strong">TRAFFIC CONTROL</span><br>
    <span class="accent">SOLUTIONS</span><br>
    <span class="strong">ENGINEERED FOR</span><br>
    <span class="accent">SAFETY.</span>
  </h1>
  <div class="hero-cta">CONTACT</div>
</section>

<h2 class="services-title">SERVICES</h2>
<p class="services-sub">SAFETY ISN’T A PRIORITY, IT’S THE FOUNDATION OF EVERYTHING WE DO</p>

<div class="hex" style="left:41px;top:575px">
  <div class="hex-photo tone-a" role="img" aria-label="Striped lane closure barricade on asphalt"></div>
  <div class="hex-label">Flagging &amp; Lane<br>Closures</div>
</div>
<div class="hex" style="left:41px;top:738px">
  <div class="hex-photo tone-f" role="img" aria-label="One lane road ahead warning sign"></div>
  <div class="hex-label">Signage &amp;<br>Barricades</div>
</div>
<div class="hex" style="left:180px;top:657px">
  <div class="hex-photo tone-b" role="img" aria-label="Slow paddle sign in a work zone"></div>
  <div class="hex-label">Temporary Traffic<br>Control Plans</div>
</div>
<div class="hex" style="left:319px;top:575px">
  <div class="hex-photo tone-c" role="img" aria-label="Red winding road warning sign by trees"></div>
  <div class="hex-label">Crash &amp; Truck<br>Mounted<br>Attenuators</div>
</div>
<div class="hex hex-feature" style="left:319px;top:738px" role="img" aria-label="Road worker in a work zone behind a warning sign">
  <div class="hex-label">Work Zone Safety Consulting for Compliance with StateDOT and FedSafe regulations</div>
</div>
<div class="hex" style="left:457px;top:657px">
  <div class="hex-photo tone-d" role="img" aria-label="Flagger ahead warning sign with traffic behind"></div>
  <div class="hex-label">Heavy Highway<br>Traffic Control</div>
</div>
<div class="hex" style="left:596px;top:574px">
  <div class="hex-photo tone-e" role="img" aria-label="Orange detour sign with arrow"></div>
  <div class="hex-label">Roadway Detours &amp;<br>Lane Shifts</div>
</div>
<div class="hex" style="left:596px;top:738px">
  <div class="hex-photo tone-g" role="img" aria-label="Cones and chain barrier at a running event"></div>
  <div class="hex-label">Event Traffic &amp;<br>Crowd Control</div>
</div>

<footer class="site-footer">
  <div class="footer-brand">ROADWISE<br>BEACON<span class="brand-bar"></span></div>
  <p class="footer-tagline">Serving Texas Industry to Ensure Safety, Compliance, and Efficient Traffic Flow.</p>
  <div class="partners">
    <span class="partner sq"></span>
    <span class="partner wide"></span>
    <span class="partner sq"></span>
    <span class="partner wide" style="width:74px;height:30px;border-radius:4px"></span>
    <span class="partner round"></span>
  </div>
  <div class="footer-divider"></div>
  <h3 class="footer-heading">Services</h3>
  <ul class="footer-list">
    <li>Road construction, maintenance, &amp; Detours</li>
    <li>Municipal &amp; State projects</li>
    <li>Private Sector &amp; Commercial Contractors</li>
    <li>Oil, Gas, Wind, Solar, &amp; Manufacturing</li>
  </ul>
  <div class="footer-rule"></div>
  <p class="copyright">©2025 ROADWISE BEACON- All rights reserved.</p>
</footer>

</body>
</html>
```